I need a very simple poster with the following quote:
"Cada escolha, uma renĂșncia, isso Ă© a vida"
Which means that to every choice there is a waiver, that's life.

It will be framed and used in my living room.

The poster has to be black and white. It is not mandatory to use commas and quotes.

The design has to be modern, like the references I posted on this board: http://pinboardly.example/marvetu/ideas/

```html
<!DOCTYPE html>
<html lang="pt">
<head>
<meta charset="utf-8">
<title>Cada escolha, uma renúncia</title>
<link href="https://fonts.googleapis.com/css2?family=Parisienne&display=swap" rel="stylesheet">
<style>
  :root {
    --page: #ffffff;
    --wall-dark: #2b2b2b;
    --wall-mid: #3a3a3a;
    --wall-light: #4a4a4a;
    --silver-light: #d4d4d4;
    --silver-mid: #a6a6a6;
    --silver-dark: #6e6e6e;
    --quote: #f4f4f4;
  }
  html, body {
    margin: 0;
    padding: 0;
    width: 1200px;
    height: 1000px;
    overflow: hidden;
    background: var(--page);
  }
  .canvas {
    position: relative;
    width: 1200px;
    height: 1000px;
    background: var(--page);
  }
  .poster {
    position: absolute;
    left: 245px;
    top: 0;
    width: 710px;
    height: 1000px;
    background: radial-gradient(ellipse at 50% 45%, var(--wall-light) 0%, var(--wall-mid) 45%, var(--wall-dark) 100%);
    overflow: hidden;
  }
  .frame-art {
    position: absolute;
    left: 0;
    top: 0;
  }
  .quote {
    position: absolute;
    left: 150px;
    top: 345px;
    margin: 0;
    font-family: "Parisienne", cursive;
    font-weight: 400;
    font-size: 62px;
    line-height: 94px;
    color: var(--quote);
    white-space: nowrap;
  }
  .quote span { display: block; }
</style>
</head>
<body>
<div class="canvas">
  <div class="poster">
    <svg class="frame-art" width="710" height="1000" viewBox="0 0 710 1000">
      <defs>
        <linearGradient id="silverBand" x1="0" y1="0" x2="1" y2="1">
          <stop offset="0" stop-color="var(--silver-light)"/>
          <stop offset="0.5" stop-color="var(--silver-mid)"/>
          <stop offset="1" stop-color="var(--silver-dark)"/>
        </linearGradient>
      </defs>
      <!-- drop shadow of the frame -->
      <rect x="70" y="138" width="567" height="720" fill="#1c1c1c" opacity="0.55"/>
      <!-- ornamental outer band -->
      <path role="img" aria-label="Ornate carved silver frame border"
            fill-rule="evenodd" fill="url(#silverBand)"
            d="M65 130 H632 V850 H65 Z M87 152 V828 H610 V152 Z"/>
      <!-- plain bevelled inner moulding -->
      <path fill-rule="evenodd" fill="var(--silver-mid)"
            d="M87 152 H610 V828 H87 Z M120 185 V795 H577 V185 Z"/>
      <rect x="98" y="163" width="501" height="654" fill="none" stroke="var(--silver-light)" stroke-width="6"/>
      <rect x="114" y="179" width="469" height="622" fill="none" stroke="var(--silver-dark)" stroke-width="4"/>
    </svg>
    <p class="quote">
      <span>Cada escolha,</span>
      <span>uma renúncia,</span>
      <span>isso é a vida</span>
    </p>
  </div>
</div>
</body>
</html>
```